Website Design for recruiting company

We need a homepage mockup for a recruiting company focused on the legal industry. Use your creative talent to come up with something visually appeal and professional for this web-site.

We'd really like to see the maze from the logo incorporated into the design somehow. Please use the website mockup provided as inspiration for this project. We really like the layout and photos!

Target Market(s)

lawyers

Industry/Entity Type

Legal

Number of Pages Required

1 page

Font styles to use
Sans Serif

```html
<!DOCTYPE html>
<html lang="en">
<head>
<meta charset="utf-8">
<title>Harborline Legal Search</title>
<link rel="stylesheet" href="https://fonts.googleapis.com/css2?family=Bebas+Neue&family=Catamaran:wght@400;500;600&family=Poppins:wght@300;400;500&display=swap">
<style>
:root{
  --ink:#1c1a1d;
  --plum:#6e626f;
  --plum-text:#6b5f6b;
  --sage:#a4b59c;
  --night:#2a2630;
  --night-deep:#1d1a20;
  --body:#5a555b;
  --white:#ffffff;
  --line:#d9d6da;
}
*{box-sizing:border-box;margin:0;padding:0}
html,body{width:1200px;height:2891px;overflow:hidden;background:var(--white)}
body{position:relative;font-family:"Poppins",sans-serif;color:var(--body)}
.abs{position:absolute}
.hero-bg{position:absolute;left:0;top:0}
.brand{position:absolute;display:flex;align-items:center;gap:12px;color:var(--white);font-family:"Catamaran",sans-serif;font-size:14px;font-weight:500}
.brand-mark{width:72px;height:72px;border-radius:50%;background:#c9c5ca;border:3px solid var(--white)}
.nav{position:absolute;left:451px;top:36px;display:flex;gap:24px;font-family:"Catamaran",sans-serif;font-size:15px;color:#e4e0e6}
.nav a{color:inherit;text-decoration:none}
.nav .active{color:var(--white);border-bottom:2px solid var(--white);padding-bottom:2px}
.pill{position:absolute;display:flex;align-items:center;justify-content:center;border-radius:30px;background:var(--plum);color:var(--white);font-family:"Catamaran",sans-serif;font-weight:500;font-size:19px;text-transform:uppercase}
.phone-pill{left:956px;top:25px;width:167px;height:46px;text-transform:none;font-family:"Poppins",sans-serif;font-weight:300;font-size:16px;gap:8px}
.hero-title{position:absolute;left:79px;top:248px;font-family:"Bebas Neue",sans-serif;font-size:58px;line-height:57px;color:var(--white);letter-spacing:.3px}
.search{position:absolute;display:flex;border-radius:30px;overflow:hidden;background:var(--white)}
.search span{flex:1;display:flex;align-items:center;padding-left:24px;font-size:14px;color:#6d686e}
.search b{display:flex;align-items:center;justify-content:center;color:var(--white);font-family:"Catamaran",sans-serif;font-weight:500;font-size:19px;border-radius:30px}
.hero-search{left:77px;top:438px;width:427px;height:50px}
.hero-search b{width:145px;background:var(--sage);border-radius:0 30px 30px 0}
.hero-photo{left:556px;top:146px;width:567px;height:600px;border-radius:46% 44% 40% 42%/38% 40% 48% 50%;background:radial-gradient(ellipse at 45% 45%,#8ea39d,#a9bbb5 60%,#e8ece9 100%)}
.section-title{position:absolute;font-family:"Catamaran",sans-serif;font-weight:500;font-size:44px;color:var(--plum-text);line-height:1}
.about-mark{left:342px;top:761px;width:73px;height:73px;border-radius:50%;background:#8a838b;border:4px solid #e6e3e6}
.about-sub{left:463px;top:812px;font-size:15px;color:var(--ink)}
.about-copy{left:468px;top:860px;width:510px;font-size:14.5px;line-height:27px}
.about-copy p+p{margin-top:10px}
.card-photo{position:absolute;top:1307px;height:396px}
.card-info{position:absolute;top:1624px;height:79px;background:var(--white);padding:18px 0 0 22px}
.card-info h3{font-family:"Catamaran",sans-serif;font-weight:500;font-size:21px;color:var(--plum-text);line-height:1.1}
.card-info p{font-size:15px;color:var(--ink);margin-top:4px}
.card-info svg{position:absolute;right:18px;top:36px}
.center{text-align:center;left:0;width:1200px}
.footer-bg{position:absolute;left:0;top:2470px}
.footer-title{left:76px;top:2605px;font-family:"Catamaran",sans-serif;font-weight:500;font-size:39px;line-height:44px;color:var(--ink)}
.footer-brand{left:801px;top:2588px}
.footer-brand .brand-mark{width:94px;height:94px;background:#a29ca3}
.contact{position:absolute;left:822px;display:flex;align-items:center;gap:14px;color:#e8e4ea;font-size:16px;font-weight:300}
</style>
</head>
<body>

<svg class="hero-bg" width="1200" height="760" viewBox="0 0 1200 760">
  <defs>
    <linearGradient id="heroTone" x1="0" y1="0" x2="1" y2="1">
      <stop offset="0" stop-color="#4a4450"/>
      <stop offset="0.5" stop-color="#2f2a35"/>
      <stop offset="1" stop-color="#1f1c24"/>
    </linearGradient>
  </defs>
  <path d="M0 0 H960 C905 280 780 600 360 674 C210 690 70 640 0 615 Z" fill="url(#heroTone)" role="img" aria-label="Smiling colleagues at a meeting, darkened background photograph"/>
</svg>

<div class="brand" style="left:77px;top:13px"><div class="brand-mark"></div>harborline legal search</div>

<nav class="nav">
  <a class="active">Home</a><a>About Us</a><a>Whats's New</a><a>For Employers</a><a>Contact Us</a>
</nav>

<div class="pill phone-pill">
  <svg width="18" height="18" viewBox="0 0 24 24" fill="none" stroke="#fff" stroke-width="2"><path d="M5 3h4l2 5-3 2a12 12 0 0 0 6 6l2-3 5 2v4a2 2 0 0 1-2 2A18 18 0 0 1 3 5a2 2 0 0 1 2-2z"/></svg>
  123 456 7890
</div>

<h1 class="hero-title">Start here,<br>let our experience<br>guide you</h1>

<div class="search hero-search"><span>Find Perfact Job</span><b>SEARCH JOB</b></div>

<div class="abs hero-photo" role="img" aria-label="Man with a laptop sitting on a sage beanbag beside a potted plant"></div>

<div class="abs about-mark"></div>
<h2 class="section-title" style="left:463px;top:762px">About Us</h2>
<p class="abs about-sub">Harborline legal Search</p>
<div class="abs about-copy">
  <p>Harborline Legal Search focuses on the permanent placement of attorneys withlaw firms and corporations in the New England area.</p>
  <p>Founded in 1982, Harborline Legal Search is the oldest attorney search firm in New England, and isranked the number one legal recruiter in New England in the most recent surveyconducted by The Counsel Review</p>
</div>
<div class="pill" style="left:468px;top:1053px;width:166px;height:52px">Learn More</div>

<h2 class="section-title" style="left:79px;top:1166px">Whats's New</h2>
<p class="abs" style="left:79px;top:1221px;width:480px;font-size:16px;line-height:23px;color:#514c52">Below are our most recent listings. All positions are in the greater Boston area unless otherwise noted.</p>

<div class="card-photo" style="left:0;width:381px;background:linear-gradient(180deg,#5d6fa6 0%,#8c8fb5 45%,#c79a63 72%,#28263a 100%)" role="img" aria-label="Waterfront hotel building at dusk"></div>
<div class="card-photo" style="left:401px;width:521px;border-radius:10px;background:linear-gradient(180deg,#3c3d40 0%,#55575a 45%,#8a7454 60%,#3a3c3c 100%)" role="img" aria-label="Modern glass office lobby with trees"></div>

<div class="card-info" style="left:152px;width:229px">
  <h3>Job Title</h3><p>New england</p>
  <svg width="24" height="12" viewBox="0 0 24 12" fill="none" stroke="#333" stroke-width="1.2"><path d="M0 6h22M17 1l5 5-5 5"/></svg>
</div>
<div class="card-info" style="left:693px;width:229px">
  <h3>Job Title</h3><p>New england</p>
  <svg width="24" height="12" viewBox="0 0 24 12" fill="none" stroke="#333" stroke-width="1.2"><path d="M0 6h22M17 1l5 5-5 5"/></svg>
</div>
<div class="pill" style="left:956px;top:1641px;width:167px;height:52px">Search Job</div>

<h2 class="section-title center abs" style="top:1783px">For Employers</h2>
<p class="abs center" style="top:1842px;font-size:15.5px;line-height:27px">Our unparalleled recruiting industry and legal experience have generated<br>anextensive network of contacts throughout the legal community.</p>

<div class="abs" style="left:287px;top:1925px;width:626px;height:385px;border-radius:14px;background:linear-gradient(135deg,#c9cfc4 0%,#e8eae6 45%,#9aa1ab 75%,#f1f1f1 100%)" role="img" aria-label="Three professionals interviewing a candidate at a table"></div>

<div class="search" style="left:349px;top:2348px;width:502px;height:51px;border:1px solid var(--line)">
  <span>Find The Right Candidate</span><b style="width:166px;background:var(--plum)">LEARN MORE</b>
</div>

<svg class="footer-bg" width="1200" height="421" viewBox="0 2470 1200 421">
  <defs>
    <linearGradient id="footTone" x1="0" y1="0" x2="1" y2="1">
      <stop offset="0" stop-color="#3a3540"/>
      <stop offset="1" stop-color="#1b181e"/>
    </linearGradient>
  </defs>
  <path d="M544 2891 C585 2650 760 2470 1000 2475 C1080 2477 1150 2490 1200 2505 V2891 Z" fill="url(#footTone)" role="img" aria-label="Dark toned photograph of people at work"/>
</svg>

<h2 class="abs footer-title">Delivering the Talent<br>Your Business Needs.</h2>
<p class="abs" style="left:79px;top:2700px;font-size:16px;color:var(--ink);letter-spacing:.3px">Harborline legal Search</p>
<div class="pill" style="left:77px;top:2739px;width:208px;height:51px">Request Talent</div>

<div class="brand footer-brand" style="font-size:15px;font-weight:400">
  <div class="brand-mark"></div>harborline legal search
</div>
<div class="contact" style="top:2702px">
  <svg width="18" height="18" viewBox="0 0 24 24" fill="#e8e4ea"><path d="M5 2h4l2 6-3 2a13 13 0 0 0 6 6l2-3 6 2v4a2 2 0 0 1-2 2A19 19 0 0 1 3 4a2 2 0 0 1 2-2z"/></svg>
  123 456 7890
</div>
<div class="contact" style="top:2742px">
  <svg width="18" height="14" viewBox="0 0 24 18"><rect width="24" height="18" rx="2" fill="#e8e4ea"/><path d="M1 2l11 8 11-8" fill="none" stroke="#2a2630" stroke-width="2"/></svg>
  hello@harborlinesearch.com
</div>
<p class="abs" style="left:813px;top:2786px;font-size:14.5px;color:#e8e4ea;font-weight:300">©NORTHGATE STUDIO -2020 All rights reserved.</p>

</body>
</html>
```